Coffee Pouch Label for Coffee Roaster

We are wanting some new labels for our coffee pouches.
We are an established, small family owned specialty coffee roaster called Tarn4 Coffee Roasters, and we are located in Kestrel Downs, VIC Australia.
Label dimensions are 100 x 150mm, to fit on a couple of different bag sizes. We use coffee pouches with kraft paper finish.
We have 3 main blends, Lanternfly, Quillrock & Pale Finch, and a range of rotating single origin coffees. We would get labels printed for the blends, but then need a 'generic' design that we can either write the name on, or stick another sticker over for the single origin coffees.
Some information that needs to be on the label:
our logo
web address: www.tarn4coffee.example
address: 47 Corvell St, Kestrel Downs, VIC
Proudly Roasted in Kestrel Downs, VIC
Blend name
our tagline/mission: act justly | love mercy | walk humbly
statement: we give $1 from every kg of coffee sold to the rescue, prevention and rehabilitation of children from slavery.
We would like to use colour to help differentiate the different blends somehow.
We are after a creative, clean design, that is representative of specialty coffee (not large commercial coffee brands).
I have uploaded our logo both with and without our tagline, and also some other packaging inspiration that i like (I quite like the meadow coffee label design).
thanks everyone!
Marcus
People who appreciate good, local coffee

```html
<!DOCTYPE html>
<html lang="en">
<head>
<meta charset="utf-8">
<title>Lanternfly – Tarn4 Coffee Roasters label</title>
<link rel="stylesheet" href="https://fonts.googleapis.com/css2?family=Cookie&family=Montserrat:wght@400;500;600;700&family=Playfair+Display:ital@1&display=swap">
<style>
  :root {
    --page: #ffffff;
    --label: #f8f4ef;
    --brown: #6a2a10;
    --brown-shadow: rgba(106, 42, 16, 0.18);
    --ink: #1d1a18;
    --muted: #77716c;
    --bean-dark: #3a1e10;
    --bean-mid: #7a4526;
    --bean-light: #a86d43;
  }
  * { margin: 0; padding: 0; box-sizing: border-box; }
  html, body {
    width: 1200px; height: 2400px; overflow: hidden;
    background: var(--page);
  }
  .canvas { position: relative; width: 1200px; height: 2400px; }
  .label {
    position: absolute; left: 60px; top: 390px;
    width: 1080px; height: 1620px;
    background: var(--label);
    overflow: hidden;
  }
  .bean-scatter { position: absolute; left: 0; top: 0; width: 1080px; height: 1620px; }
  .blend-name {
    position: absolute; left: 0; width: 1080px; top: 265px;
    text-align: center;
    font-family: "Cookie", cursive; font-weight: 400;
    font-size: 205px; line-height: 1;
    color: var(--brown);
    text-shadow: 4px 5px 0 var(--brown-shadow);
  }
  .origin {
    position: absolute; left: 0; width: 1080px; top: 535px;
    text-align: center;
    font-family: "Montserrat", sans-serif; font-weight: 500;
    font-size: 29px; color: var(--ink);
  }
  .mission {
    position: absolute; left: 441px; top: 640px;
    font-family: "Playfair Display", serif; font-style: italic;
    font-size: 66px; line-height: 84px; color: var(--ink);
    list-style: none;
  }
  .pledge {
    position: absolute; left: 441px; top: 935px; width: 500px;
    font-family: "Montserrat", sans-serif; font-weight: 500;
    font-size: 23px; line-height: 33px; color: var(--ink);
  }
  .pledge strong { font-weight: 700; }
  .brand {
    position: absolute; right: 150px; top: 1168px;
    display: flex; align-items: center; gap: 16px;
    font-family: "Montserrat", sans-serif; font-weight: 700;
    font-size: 34px; color: var(--ink); white-space: nowrap;
  }
  .brand-dot { width: 26px; height: 26px; border-radius: 50%; background: var(--ink); }
  .contact {
    position: absolute; right: 150px; top: 1272px;
    font-family: "Montserrat", sans-serif; color: var(--muted);
    font-size: 22px; line-height: 33px;
    list-style: none;
  }
  .contact li { display: flex; align-items: center; gap: 10px; }
  .contact .web { font-weight: 600; font-size: 24px; }
  .contact svg { width: 20px; height: 20px; }
  .weight {
    position: absolute; right: 150px; top: 1400px;
    font-family: "Playfair Display", serif; font-style: italic;
    font-size: 62px; color: var(--brown);
  }
</style>
</head>
<body>
<main class="canvas">
  <section class="label">
    <svg class="bean-scatter" viewBox="0 0 1080 1620" role="img" aria-label="Photo of roasted coffee beans scattered across the lower left corner">
      <defs>
        <linearGradient id="beanTone" x1="0" y1="0" x2="1" y2="1">
          <stop offset="0" stop-color="var(--bean-mid)"/>
          <stop offset="0.5" stop-color="var(--bean-light)"/>
          <stop offset="1" stop-color="var(--bean-dark)"/>
        </linearGradient>
      </defs>
      <path d="M0 550 C80 570 170 610 210 700 C250 820 250 930 300 1040 C360 1170 450 1270 560 1340 C640 1400 720 1460 780 1540 L830 1620 L0 1620 Z" fill="url(#beanTone)"/>
    </svg>

    <h1 class="blend-name">Lanternfly</h1>
    <p class="origin">Proudly Roasted in Kestrel Downs, VIC</p>

    <ul class="mission">
      <li>Act justly</li>
      <li>Love mercy</li>
      <li>Walk humbly</li>
    </ul>

    <p class="pledge">we give <strong>$1</strong> from every kg of coffee sold to the rescue, prevention and rehabilitation of children from slavery.</p>

    <div class="brand"><span class="brand-dot"></span>Tarn4 Coffee Roasters</div>

    <ul class="contact">
      <li>
        <svg viewBox="0 0 20 20" aria-hidden="true"><path d="M10 1.5a6 6 0 0 0-6 6c0 4.5 6 11 6 11s6-6.5 6-11a6 6 0 0 0-6-6z" fill="none" stroke="currentColor" stroke-width="2"/><circle cx="10" cy="7.5" r="2" fill="currentColor"/></svg>
        47 Corvell St, Kestrel Downs, VIC
      </li>
      <li class="web">
        <svg viewBox="0 0 20 20" aria-hidden="true"><circle cx="10" cy="10" r="8" fill="none" stroke="currentColor" stroke-width="1.6"/><ellipse cx="10" cy="10" rx="3.5" ry="8" fill="none" stroke="currentColor" stroke-width="1.4"/><path d="M2 10h16M3.5 6h13M3.5 14h13" stroke="currentColor" stroke-width="1.2"/></svg>
        www.tarn4coffee.example
      </li>
    </ul>

    <p class="weight">12 oz</p>
  </section>
</main>
</body>
</html>
```